Bref créative
Business card design for dental office
appointment card
Professional
Carla Vostrikov, D.M.D.
4817 Route 92 Building D
Dunmore Bay, NJ 08914
carladmd@velmora.net
Appointment Date and Time

```html
<!DOCTYPE html>
<html lang="en">
<head>
<meta charset="utf-8">
<title>Clearwave Dental – Business & Appointment Card</title>
<link rel="stylesheet" href="https://fonts.googleapis.com/css2?family=Cinzel:wght@400;600&family=Arimo:wght@400;700&display=swap">
<style>
  :root {
    --backdrop: #2b2b2d;
    --card: #ffffff;
    --card-edge: #e4e6ea;
    --brand-blue: #1f4f9a;
    --brand-green: #3f9b35;
    --ink: #333333;
    --rule: #555555;
    --divider: #c9ccd2;
  }
  * { margin: 0; padding: 0; box-sizing: border-box; }
  html, body { width: 1200px; height: 883px; overflow: hidden; }
  body { background: var(--backdrop); position: relative; }

  .card {
    position: absolute;
    background: linear-gradient(160deg, var(--card) 60%, var(--card-edge));
    border-radius: 28px;
    overflow: hidden;
    box-shadow: 0 8px 24px rgba(0,0,0,.45);
  }

  /* Front */
  .card--front { left: 137px; top: 86px; width: 600px; height: 350px; }
  .brand-name {
    position: absolute;
    font-family: 'Cinzel', serif; font-weight: 600;
    color: var(--brand-blue); white-space: nowrap;
  }
  .card--front .brand-name { left: 0; width: 100%; text-align: center; top: 44px; font-size: 34px; }
  .holder-name {
    position: absolute; left: 31px; top: 216px;
    font-family: 'Cinzel', serif; font-size: 17px; color: var(--brand-blue); white-space: nowrap;
  }
  .divider {
    position: absolute; left: 326px; top: 178px; width: 1px; height: 144px;
    background: var(--divider);
  }
  .contact {
    position: absolute; left: 348px; top: 176px;
    font-family: 'Cinzel', serif; font-size: 13px; color: var(--ink); line-height: 19px; white-space: nowrap;
  }
  .contact-list { list-style: none; margin-top: 12px; }
  .contact-list li { display: flex; align-items: center; gap: 9px; height: 21px; }
  .contact-list svg { width: 14px; height: 12px; fill: none; stroke: var(--ink); stroke-width: 1.4; }
  .band { position: absolute; top: 322px; height: 28px; }
  .band--blue { left: 0; width: 326px; background: var(--brand-blue); }
  .band--green { left: 334px; right: 0; background: var(--brand-green); }

  /* Back */
  .card--back { left: 470px; top: 473px; width: 593px; height: 367px; }
  .appt-title {
    position: absolute; left: 56px; top: 44px;
    font-family: 'Arimo', sans-serif; font-weight: 700; font-size: 22px; color: #111;
    border-bottom: 2px solid #111; line-height: 25px; white-space: nowrap;
  }
  .field {
    position: absolute; left: 56px; display: flex; align-items: flex-end;
    font-family: 'Arimo', sans-serif; font-size: 15px; color: #111; white-space: nowrap;
  }
  .field .label { width: 57px; }
  .field .label--time { width: 48px; margin-left: 19px; }
  .field .line { border-bottom: 2px dotted var(--rule); height: 14px; }
  .line--date { width: 173px; }
  .line--time { width: 185px; }
  .line--note { width: 425px; }
  .card--back .brand-name { right: 54px; top: 296px; font-size: 18px; }
</style>
</head>
<body>
  <section class="card card--front" aria-label="Business card front">
    <div class="brand-name">Clearwave Dental</div>
    <div class="holder-name">Carla Vostrikov, D.M.D.</div>
    <div class="divider"></div>
    <div class="contact">
      <div>4817 Route 92 Building D</div>
      <div>Dunmore Bay, NJ 08914</div>
      <ul class="contact-list">
        <li><svg viewBox="0 0 15 13"><path d="M2 4q5.5-4 11 0l-2 2-2-1v-1H6v1L4 6z M3 7h9v5H3z"/></svg>(732) 555-0148</li>
        <li><svg viewBox="0 0 15 13"><rect x="2" y="1" width="11" height="11"/><path d="M4 4h7M4 7h7"/></svg>(732) 555-0172</li>
        <li><svg viewBox="0 0 15 13"><rect x="1" y="2" width="13" height="9"/><path d="M1 2l6.5 5L14 2"/></svg>carladmd@velmora.net</li>
      </ul>
    </div>
    <div class="band band--blue"></div>
    <div class="band band--green"></div>
  </section>

  <section class="card card--back" aria-label="Appointment card">
    <div class="appt-title">Your Next Appointment is on:</div>
    <div class="field" style="top:90px;"><span class="label">Date :</span><span class="line line--date"></span><span class="label label--time">Time :</span><span class="line line--time"></span></div>
    <div class="field" style="top:133px;"><span class="label">Date :</span><span class="line line--date"></span><span class="label label--time">Time :</span><span class="line line--time"></span></div>
    <div class="field" style="top:176px;"><span class="label">Note :</span><span class="line line--note"></span></div>
    <div class="field" style="top:224px; left:113px;"><span class="line line--note"></span></div>
    <div class="brand-name">Clearwave Dental</div>
  </section>
</body>
</html>
```